Advertisement Design Project

Money Nest is a financial services provider operating a network of 50+ payday loan and check cashing centers across Ontario.

We are launching a special promotion for our Payday Loan product.

Specifically, the promotion is a "New Customer Acquisition Strategy” whereby we are incentifying new customers who have not had a payday loan with us.

Design: “Penny Week - $100 Loan for $ 1 - First Loan”

The promotion is a $100 payday loan for $1.

We want to create a unique trademark/emblem/icon to advertise our ‘Penny Week’ promotion.

The design will be placed in the form of a window decal on our store front windows and on flyers, etc.

With respect to choice of color, we are looking for something that will grab motorists and walk by traffic when they look at our store front.

Our company colors are red/black on Yellow, however, this Point of Purchase decal does not necessarily have to be the branded the same unless you feel this color is more impactful than others.

We certainly want the “$100 loan for $1” to the center point of the design.

Since this is a decal the design does not necessarily have to be a box or rectangle…certain words/phrases, etc. can protrude outside of the design.

In general we have two decal sizes, 2 feet in diameter and 3 feet in diameter (depending on the store front windows of some of our branches).

Also, the emblem/icon/logo needs to have some fine print [somewhere towards the bottom]

*Offer applies to first time Payday Loan customers only, or customers that have not initiated a Payday Loan in the last 12 months prior to the present date. Not valid with any other offers
and valid at participating Money Nest locations only. Limit one offer per customer. Limited time offer. The cost of borrowing at Money Nest is $21 per each $100 advanced. On a $300 loan for 14 days, the cost of borrowing is $63, with a total payback amount of $363. The maximum allowable cost of borrowing under payday loan agreements is $21 per each $100 advanced.

Thanks,
Tomas

Industry/Entity Type

Financial

```html
<!DOCTYPE html>
<html lang="en">
<head>
<meta charset="utf-8">
<title>Penny Week – $100 Loan for $1</title>
<link rel="stylesheet" href="https://fonts.googleapis.com/css2?family=Lilita+One&family=Anton&family=Arimo:wght@400;700&display=swap">
<style>
  :root {
    --bg: #000000;
    --red: #e3141b;
    --yellow: #ffd200;
    --yellow-light: #fff48a;
    --yellow-deep: #f7b800;
    --white: #ffffff;
    --ink: #111111;
  }
  html, body {
    margin: 0;
    padding: 0;
    width: 1054px;
    height: 1200px;
    overflow: hidden;
    background: var(--bg);
  }
  .decal {
    position: relative;
    width: 1054px;
    height: 1200px;
  }
  .decal__disc {
    position: absolute;
    left: 0;
    top: 0;
  }
  .promo-title {
    position: absolute;
    left: 0;
    width: 1054px;
    top: 130px;
    margin: 0;
    text-align: center;
    font-family: "Lilita One", sans-serif;
    font-weight: 400;
    font-size: 128px;
    line-height: 1;
    color: var(--red);
    letter-spacing: -1px;
  }
  .offer-line {
    position: absolute;
    top: 300px;
    left: 0;
    width: 1054px;
    display: flex;
    justify-content: center;
    align-items: center;
    gap: 16px;
  }
  .offer-line__amount {
    background: var(--red);
    color: var(--white);
    font-family: "Anton", sans-serif;
    font-size: 72px;
    line-height: 1;
    padding: 6px 12px 8px;
    border-radius: 4px;
  }
  .offer-line__label {
    font-family: "Anton", sans-serif;
    font-size: 108px;
    line-height: 1;
    color: var(--ink);
    letter-spacing: 1px;
  }
  .offer-price {
    position: absolute;
    top: 420px;
    left: 0;
    width: 1054px;
    display: flex;
    justify-content: center;
    align-items: center;
    gap: 22px;
  }
  .offer-price__value {
    margin: 0;
    font-family: "Anton", sans-serif;
    font-size: 360px;
    line-height: 0.9;
    color: var(--red);
    letter-spacing: -6px;
    transform: skewX(-8deg);
  }
  .offer-price__sign {
    font-size: 290px;
  }
  .offer-price__note {
    margin: 0;
    font-family: "Anton", sans-serif;
    font-size: 34px;
    line-height: 1;
    color: var(--ink);
    white-space: nowrap;
  }
  .credit-note {
    position: absolute;
    top: 738px;
    left: 0;
    width: 1054px;
    text-align: center;
    margin: 0;
    font-family: "Anton", sans-serif;
    font-size: 66px;
    line-height: 1;
    color: var(--ink);
    letter-spacing: 0.5px;
  }
  .fine-print {
    position: absolute;
    top: 850px;
    left: 217px;
    width: 626px;
    margin: 0;
    font-family: "Arimo", sans-serif;
    font-size: 16px;
    line-height: 1.4;
    color: var(--ink);
    text-align: center;
  }
</style>
</head>
<body>
<main class="decal">
  <svg class="decal__disc" width="1054" height="1200" viewBox="0 0 1054 1200" aria-hidden="true">
    <defs>
      <radialGradient id="burst" cx="50%" cy="42%" r="60%">
        <stop offset="0%" stop-color="var(--yellow-light)"/>
        <stop offset="55%" stop-color="var(--yellow)"/>
        <stop offset="100%" stop-color="var(--yellow-deep)"/>
      </radialGradient>
      <clipPath id="disc-clip">
        <circle cx="530" cy="720" r="452"/>
      </clipPath>
    </defs>
    <circle cx="530" cy="720" r="468" fill="var(--white)"/>
    <g clip-path="url(#disc-clip)">
      <rect x="70" y="260" width="920" height="920" fill="url(#burst)"/>
      <path d="M70 838 Q530 796 990 838 L990 1180 L70 1180 Z" fill="var(--white)"/>
      <path d="M70 834 Q530 790 990 834" fill="none" stroke="var(--red)" stroke-width="12"/>
    </g>
  </svg>

  <h1 class="promo-title">Penny Week</h1>

  <div class="offer-line">
    <span class="offer-line__amount">$100</span>
    <span class="offer-line__label">LOAN FOR</span>
  </div>

  <div class="offer-price">
    <p class="offer-price__value"><span class="offer-price__sign">$</span>1</p>
    <p class="offer-price__note">ON FIRST LOAN</p>
  </div>

  <p class="credit-note">NO CREDIT CHECKS</p>

  <p class="fine-print">*Details In-Store. Limited Time Offer. Without this promo, the cost of borrowing at Money Nest is $21 per each $100 advanced. On a $300 loan for 14 days, the cost of borrowing is $63, with a total payback amount of $363. The maximum allowable cost of borrowing under payday loan agreements is $21 per each $100 advanced.</p>
</main>
</body>
</html>
```